Homepage for preschool with coding and branding

Homepage for preschool

1. Homepage with:
- Large top section
- 3 columns below for the 3 main services
- A section to have an instagram feed of the school account
- Find / us map, contact info
- Footer

Standard header with menu
Standard footer

Please see current site

https://qlnk.example/7PRTvz4

New design must not be 'identical' to this.. must improve but match,

Target Market(s)

young moms in florida

Coding

Coded - Design and coding required

Number of Pages Required

2 page

Font styles to use
Sans Serif

Requirements
Must have
• - Match colors provided
- Match the 'style' of the logo across the site.

We use BuddyPress so must work with it.

```html
<!DOCTYPE html>
<html lang="en">
<head>
<meta charset="utf-8">
<title>Little Comets – Fun & Safe Daycare</title>
<link href="https://fonts.googleapis.com/css2?family=Poppins:wght@400;500;600;700;800&family=Open+Sans:wght@400;600&display=swap" rel="stylesheet">
<style>
:root{
  --blue:#1b9bd8;
  --blue-dark:#0f7fb8;
  --yellow:#f6c21a;
  --ink:#222428;
  --grey:#6b6f76;
  --cream:#fbf5cf;
  --dark:#2a2a2d;
  --white:#ffffff;
}
*{box-sizing:border-box;margin:0;padding:0}
html,body{width:1200px;height:3792px;overflow:hidden}
body{font-family:"Open Sans",Arial,sans-serif;color:var(--ink);background:var(--white);position:relative}
h1,h2,h3,h4,.nav,.btn,.brand{font-family:"Poppins",Arial,sans-serif}

/* header */
.site-header{position:absolute;top:0;left:0;width:1200px;height:120px;z-index:5}
.brand{position:absolute;left:40px;top:22px;display:flex;align-items:center;gap:12px;font-weight:800;font-size:30px;color:var(--yellow)}
.brand-dot{width:54px;height:54px;border-radius:50%;background:var(--yellow)}
.account{position:absolute;right:160px;top:8px;display:flex;gap:8px}
.account a{font:600 13px "Poppins",sans-serif;color:#fff;padding:5px 18px;border-radius:3px;background:var(--blue);text-decoration:none}
.account a.signup{background:#e7453c}
.navbar{position:absolute;left:480px;top:46px;width:700px;height:72px;background:#fff;display:flex;align-items:center;border-radius:0 0 0 4px}
.nav{display:flex;gap:28px;padding-left:30px;font-size:15px;font-weight:500;white-space:nowrap}
.nav a{color:var(--ink);text-decoration:none}
.callus{position:absolute;right:16px;top:8px;background:var(--blue);color:#fff;padding:8px 16px;border-radius:3px;font:600 12px "Poppins",sans-serif;line-height:1.3}
.callus strong{display:block;font-size:16px}

/* hero */
.hero{position:absolute;top:0;left:0;width:1200px;height:880px;overflow:hidden}
.hero-photo{position:absolute;inset:0;background:linear-gradient(100deg,#3d6b2f 0%,#6e8c3f 35%,#c79a63 60%,#8fa65a 80%,#4f7a36 100%)}
.hero-shade{position:absolute;inset:0;background:linear-gradient(90deg,rgba(0,0,0,.45),rgba(0,0,0,0) 60%)}
.hero-copy{position:absolute;left:150px;top:228px;color:#fff}
.hero-copy h1{font-size:72px;line-height:1.08;font-weight:700}
.hero-copy p{font-size:18px;margin-top:26px;line-height:1.5;width:520px}
.btn{display:inline-block;background:var(--blue);color:#fff;font-weight:600;font-size:14px;padding:12px 26px;border-radius:4px;text-decoration:none}
.hero-copy .btn{margin-top:26px}
.hero-curve{position:absolute;left:0;bottom:0;width:1200px;height:120px}

/* services */
.services{position:absolute;top:672px;left:152px;width:880px;display:flex;gap:32px;z-index:3}
.service{width:272px;height:330px;border-radius:12px;overflow:hidden;color:#fff;box-shadow:0 10px 24px rgba(0,0,0,.15)}
.service.blue{background:var(--blue)}
.service.black{background:var(--dark)}
.service.yellow{background:var(--yellow)}
.service h3{font-size:22px;font-weight:600;padding:26px 22px 10px}
.service p{font-size:14px;line-height:1.5;padding:0 22px}
.service .photo{margin:18px 14px 0;height:156px;border-radius:50% 50% 10px 10px/30% 30% 10px 10px;background:linear-gradient(135deg,#e7b27a,#c46e4a 55%,#6d9bc4)}

/* mission */
.mission{position:absolute;top:1060px;left:0;width:1200px;height:520px}
.mission-photo{position:absolute;left:150px;top:0;width:420px;height:380px;border-radius:46% 54% 42% 58%/52% 44% 56% 48%;background:linear-gradient(140deg,var(--yellow) 0%,#f2a45c 40%,#7fb3da 100%)}
.mission-copy{position:absolute;left:625px;top:70px;width:440px}
h2.title{font-size:42px;font-weight:700;letter-spacing:.5px}
h2.title span{color:var(--blue)}
.mission-copy p{font-size:15px;line-height:1.65;color:var(--grey);margin:22px 0 28px}
.kid-left{position:absolute;left:120px;top:380px;width:110px;height:110px;border-radius:50%;background:linear-gradient(135deg,#f7d36a,#e88c5a)}
.kid-right{position:absolute;left:1060px;top:440px;width:100px;height:100px;border-radius:50%;background:linear-gradient(135deg,#9fd3f0,#5aa2d6)}

/* why choose */
.why{position:absolute;top:1560px;left:0;width:1200px;height:640px}
.why svg.band{position:absolute;inset:0}
.why-inner{position:absolute;top:140px;left:0;width:1200px;text-align:center;color:#fff}
.why-inner h2{font-size:44px;font-weight:700}
.why-inner > p{width:560px;margin:18px auto 0;font-size:17px;line-height:1.55}
.features{display:flex;justify-content:center;gap:80px;margin-top:50px}
.feature{width:240px}
.feature svg{width:64px;height:64px}
.feature h4{font-size:22px;font-weight:500;margin:14px 0 8px}
.feature p{font-size:14px;line-height:1.5}

/* testimonials */
.parents{position:absolute;top:2200px;left:0;width:1200px;height:460px;text-align:center}
.parents h2{margin-top:24px}
.quotes{display:flex;justify-content:center;gap:40px;margin-top:40px}
.quote{width:420px;height:300px;background:var(--cream);position:relative;padding:36px 40px 0;text-align:left}
.quote .mark{position:absolute;left:14px;top:18px;font:700 40px "Poppins",sans-serif;color:var(--blue);line-height:1}
.quote p{font-size:14px;line-height:1.6;color:var(--grey)}
.quote .avatar{width:74px;height:74px;border-radius:50%;background:linear-gradient(135deg,#e9b889,#a46a4a);margin:24px auto 8px;border:4px solid #fff}
.quote .who{text-align:center;font:500 15px "Poppins",sans-serif;color:var(--ink)}

/* gallery */
.gallery{position:absolute;top:2660px;left:0;width:1200px;height:620px;background:linear-gradient(160deg,#3a3430,#5b4a3a 45%,#2d3a45)}
.gallery-veil{position:absolute;inset:0;background:rgba(20,20,22,.55)}
.gallery h2{position:absolute;top:40px;width:100%;text-align:center;color:#fff}
.gallery h2 span{color:var(--yellow)}
.grid{position:absolute;top:160px;left:150px;width:900px;display:grid;grid-template-columns:repeat(5,1fr);gap:14px}
.grid div{height:170px;border-radius:6px;border:4px solid #fff}
.g1{background:linear-gradient(135deg,#f2c66a,#d8834e)}
.g2{background:linear-gradient(135deg,#f5d0b0,#c98d6c)}
.g3{background:linear-gradient(135deg,#cfe0ea,#8fb6cc)}
.g4{background:linear-gradient(135deg,#e8d6c0,#a88a6a)}
.g5{background:linear-gradient(135deg,#f4d9e0,#c98da2)}
.g6{background:linear-gradient(135deg,#f7e08a,#e59a4c)}
.g7{background:linear-gradient(135deg,#e4b89a,#9c6a50)}
.g8{background:linear-gradient(135deg,#d9ecf5,#79aacb)}
.g9{background:linear-gradient(135deg,#f1c6a2,#c57a55)}
.g10{background:linear-gradient(135deg,#f6e6b0,#d7a85c)}

/* contact */
.contact{position:absolute;top:3280px;left:0;width:1200px;height:200px;background:#fff}
.contact-cards{position:absolute;top:30px;left:180px;width:840px;display:flex;justify-content:space-between}
.ccard{width:250px;height:130px;background:var(--blue);border-radius:6px;color:#fff;text-align:center;position:relative;padding-top:34px}
.ccard .ico{position:absolute;top:-26px;left:50%;margin-left:-26px;width:52px;height:52px;border-radius:50%;background:var(--yellow);display:flex;align-items:center;justify-content:center}
.ccard h4{font-size:20px;font-weight:600}
.ccard p{font-size:12px;line-height:1.45;margin-top:6px;padding:0 16px}

/* footer */
.site-footer{position:absolute;top:3480px;left:0;width:1200px;height:312px;background:var(--dark);color:#fff}
.f-brand{position:absolute;left:150px;top:40px;display:flex;align-items:center;gap:10px;font:800 22px "Poppins",sans-serif;color:var(--yellow);white-space:nowrap}
.f-brand i{width:54px;height:54px;border-radius:50%;background:var(--yellow);display:block}
.f-col{position:absolute;top:40px;font:500 13px "Poppins",sans-serif;line-height:2.1;white-space:nowrap}
.f-col h4{font-size:14px;font-weight:600;margin-bottom:2px}
.f-col a{color:#ddd;text-decoration:none;display:block}
.f-map{position:absolute;left:850px;top:40px;width:200px;height:110px;border-radius:4px;background:linear-gradient(135deg,#e9ece4,#cfd8c4)}
.socials{position:absolute;top:210px;left:0;width:100%;display:flex;justify-content:center;gap:12px}
.socials span{width:30px;height:30px;border-radius:50%;border:2px solid #bbb}
.copyright{position:absolute;bottom:0;width:100%;height:44px;border-top:1px solid #3c3c40;text-align:center;font-size:13px;line-height:44px;color:#aaa}
</style>
</head>
<body>

<section class="hero">
  <div class="hero-photo" role="img" aria-label="Photo of children blowing soap bubbles outdoors"></div>
  <div class="hero-shade"></div>
  <div class="hero-copy">
    <h1>Fun &amp; Safe<br>Daycare</h1>
    <p>We offer high quality Daycare Services, contact us or visit us today for more information</p>
    <a class="btn" href="#">GET STARTED</a>
  </div>
  <svg class="hero-curve" viewBox="0 0 1200 120" preserveAspectRatio="none"><path d="M0 70 Q600 150 1200 40 L1200 120 L0 120Z" fill="#fff"/></svg>
</section>

<header class="site-header">
  <div class="brand"><span class="brand-dot"></span>Little Comets</div>
  <div class="account"><a href="#">Login</a><a class="signup" href="#">Sign Up</a></div>
  <div class="navbar">
    <nav class="nav"><a href="#">Mommy &amp; Me</a><a href="#">Kid Comets</a><a href="#">Kid Comets Online</a><a href="#">Contact</a></nav>
    <div class="callus">CALL US<strong>(555) 014-2290</strong></div>
  </div>
</header>

<section class="services">
  <article class="service blue"><h3>Preschool</h3><p>Lorem Ipsum is simply dummy text of the printing and typesetting industry.</p><div class="photo" role="img" aria-label="Photo of preschool children at a table"></div></article>
  <article class="service black"><h3>Quality daycare</h3><p>Lorem Ipsum is simply dummy text of the printing and typesetting industry.</p><div class="photo" role="img" aria-label="Photo of children playing in daycare"></div></article>
  <article class="service yellow"><h3>Talented Staff</h3><p>Lorem Ipsum is simply dummy text of the printing and typesetting industry.</p><div class="photo" role="img" aria-label="Photo of teacher with a group of children"></div></article>
</section>

<section class="mission">
  <div class="mission-photo" role="img" aria-label="Photo of children reading with a teacher"></div>
  <div class="kid-left" role="img" aria-label="Illustration of a child playing"></div>
  <div class="kid-right" role="img" aria-label="Illustration of a child running"></div>
  <div class="mission-copy">
    <h2 class="title">OUR <span>MISSION</span></h2>
    <p>Since opening we have been a professional and experienced early learning center that delivers caring results in all aspects of childhood growth. We work throughout the area and its neighborhoods. We pride ourselves on excellent care and attention to detail. We use only top quality materials to ensure an outstanding and long-lasting start, using both traditional and modern techniques.</p>
    <a class="btn" href="#">Read More</a>
  </div>
</section>

<section class="why">
  <svg class="band" viewBox="0 0 1200 640" preserveAspectRatio="none">
    <path d="M0 110 Q600 -30 1200 110 L1200 640 L0 640Z" fill="var(--yellow)"/>
    <path d="M0 122 Q600 -14 1200 122 L1200 640 L0 640Z" fill="var(--blue)"/>
  </svg>
  <div class="why-inner">
    <h2>WHY CHOOSE US?</h2>
    <p>Lorem Ipsum is simply dummy text of the printing and typesetting industry. Lorem Ipsum has been the industry's standard dummy text.</p>
    <div class="features">
      <div class="feature">
        <svg viewBox="0 0 64 64" fill="none" stroke="#fff" stroke-width="3"><path d="M12 14h18v38H12zM34 14h18v38H34z"/><path d="M16 24h10M38 24h10M16 32h10M38 32h10"/></svg>
        <h4>Active Learning</h4><p>Lorem Ipsum is simply dummy text of the printing and typesetting industry.</p>
      </div>
      <div class="feature">
        <svg viewBox="0 0 64 64" fill="none" stroke="#fff" stroke-width="3"><path d="M32 8l20 8v16c0 12-9 20-20 24-11-4-20-12-20-24V16z"/><path d="M23 32l7 7 12-13"/></svg>
        <h4>Safe Enviroment</h4><p>Lorem Ipsum is simply dummy text of the printing and typesetting industry.</p>
      </div>
      <div class="feature">
        <svg viewBox="0 0 64 64" fill="none" stroke="#fff" stroke-width="3"><circle cx="32" cy="22" r="10"/><path d="M14 54c0-10 8-18 18-18s18 8 18 18"/></svg>
        <h4>Qualified teachers</h4><p>Lorem Ipsum is simply dummy text of the printing and typesetting industry.</p>
      </div>
    </div>
  </div>
</section>

<section class="parents">
  <h2 class="title">WHAT <span>PARENTS SAY</span></h2>
  <div class="quotes">
    <div class="quote"><span class="mark">“</span><p>Our little one settled in so quickly and comes home happy every single day. The teachers are warm, patient and always keep us updated on progress. We could not ask for a better start.</p><div class="avatar" role="img" aria-label="Parent portrait"></div><div class="who">Client Name</div></div>
    <div class="quote"><span class="mark">“</span><p>Our little one settled in so quickly and comes home happy every single day. The teachers are warm, patient and always keep us updated on progress. We could not ask for a better start.</p><div class="avatar" role="img" aria-label="Parent portrait"></div><div class="who">Client Name</div></div>
  </div>
</section>

<section class="gallery" role="img" aria-label="Background photo of colourful toy blocks">
  <div class="gallery-veil"></div>
  <h2 class="title">OUR <span>GALLERY</span></h2>
  <div class="grid">
    <div class="g1" role="img" aria-label="Gallery photo of a child"></div>
    <div class="g2" role="img" aria-label="Gallery photo of a child"></div>
    <div class="g3" role="img" aria-label="Gallery photo of a baby"></div>
    <div class="g4" role="img" aria-label="Gallery photo of children playing"></div>
    <div class="g5" role="img" aria-label="Gallery photo of a child"></div>
    <div class="g6" role="img" aria-label="Gallery photo of a child with toys"></div>
    <div class="g7" role="img" aria-label="Gallery photo of a child"></div>
    <div class="g8" role="img" aria-label="Gallery photo of a child stacking blocks"></div>
    <div class="g9" role="img" aria-label="Gallery photo of a baby"></div>
    <div class="g10" role="img" aria-label="Gallery photo of a child playing"></div>
  </div>
</section>

<section class="contact">
  <div class="contact-cards">
    <div class="ccard"><span class="ico"><svg width="26" height="26" viewBox="0 0 24 24" fill="none" stroke="#fff" stroke-width="2"><rect x="3" y="5" width="18" height="14" rx="1"/><path d="M3 6l9 7 9-7"/></svg></span><h4>Write Us</h4><p>hello@littlecomets.example</p></div>
    <div class="ccard"><span class="ico"><svg width="26" height="26" viewBox="0 0 24 24" fill="none" stroke="#fff" stroke-width="2"><path d="M12 22s7-7 7-12a7 7 0 00-14 0c0 5 7 12 7 12z"/><circle cx="12" cy="10" r="2.5"/></svg></span><h4>Visit Us</h4><p>Harbor Walk Plaza, 1200 Bayview Rd, Ste 4, Coral Point FL 33000</p></div>
    <div class="ccard"><span class="ico"><svg width="26" height="26" viewBox="0 0 24 24" fill="none" stroke="#fff" stroke-width="2"><path d="M5 3h4l2 5-3 2a11 11 0 006 6l2-3 5 2v4a2 2 0 01-2 2A17 17 0 013 5a2 2 0 012-2z"/></svg></span><h4>Call Us</h4><p>(555) 014-2290</p></div>
  </div>
</section>

<footer class="site-footer">
  <div class="f-brand"><i></i>Little Comets</div>
  <div class="f-col" style="left:430px"><a href="#">MOMMY &amp; ME</a><a href="#">KID COMETS</a><a href="#">KID COMETS ONLINE</a><a href="#">CONTACT</a></div>
  <div class="f-col" style="left:610px"><h4>SERVICES</h4><a href="#">Prek</a><a href="#">Camps</a><a href="#">News</a></div>
  <div class="f-col" style="left:720px"><h4>QUICK LINKS</h4><a href="#">FAQ</a><a href="#">Testimonials</a><a href="#">Sitemap</a></div>
  <div class="f-map" role="img" aria-label="Map showing the school location"></div>
  <div class="socials"><span></span><span></span><span></span><span></span></div>
  <div class="copyright">© 2020 Little Comets. All Rights are Reserved.</div>
</footer>

</body>
</html>
```